Maple Hollow Bloom Panels Business card

Looking to have a business card design incorporating my logo for my flower wall business.

Industry/Entity Type

Wedding & event planning

Contact Information for Business Card

My business logo, my name - Lena Whitcombe (owner), my tagline - Let us be your something extra, phone # 401-726-3148, email address - maplehollowbloompanels@mailvane.net, my website - maplehollowbloompanels.net, Instagram handle- @maplehollowbloompanels, FB handle Handle - maplehollowbloompanels

Font styles to use
Other font styles liked:
• Sentaina is the font that is used in my logo

Requirements
Must have
• Would like a double sided business card

```html
<!DOCTYPE html>
<html lang="en">
<head>
<meta charset="utf-8">
<title>Maple Hollow Bloom Panels – Business Card</title>
<link href="https://fonts.googleapis.com/css2?family=Great+Vibes&family=Raleway:wght@400;500;600;700&display=swap" rel="stylesheet">
<style>
  :root {
    --blush: #f9dce8;
    --rose: #e497c2;
    --rose-text: #e68ab9;
    --gold: #d9b548;
    --sage: #5b7257;
    --ink: #2b2b2b;
    --paper: #ffffff;
    --stage: #8f8d89;
  }
  * { margin: 0; padding: 0; box-sizing: border-box; }
  html, body { width: 1200px; height: 2643px; overflow: hidden; }
  body { position: relative; background: var(--paper); font-family: "Raleway", sans-serif; color: var(--ink); }

  .stage { position: absolute; left: 0; top: 0; width: 1200px; height: 900px; background: var(--stage); }

  .card { position: absolute; width: 420px; height: 735px; background: var(--paper); overflow: hidden; box-shadow: 0 6px 14px rgba(0,0,0,.18); }
  .card--mini { transform: scale(0.738); transform-origin: 0 0; }
  .card svg.shape { position: absolute; left: 0; top: 0; }

  .brand-circle { position: absolute; border-radius: 50%; background: var(--paper); display: flex; align-items: center; justify-content: center; text-align: center; }
  .brand-name { font-family: "Raleway", sans-serif; font-weight: 600; color: var(--ink); letter-spacing: .12em; line-height: 1.35; }

  .front .brand-circle { left: 52px; top: 57px; width: 316px; height: 316px; }
  .front .brand-name { font-size: 26px; width: 220px; }
  .tagline { position: absolute; left: 0; width: 420px; text-align: center; font-family: "Great Vibes", cursive; color: var(--sage); }
  .tagline--main { top: 455px; font-size: 64px; }
  .tagline--sub { top: 538px; font-size: 32px; color: var(--ink); }
  .tagline--sub .dot { display: inline-block; width: 8px; height: 8px; border-radius: 50%; background: var(--rose); vertical-align: middle; margin: 0 12px; }
  .web-pill { position: absolute; left: 57px; top: 660px; width: 308px; height: 26px; border-radius: 13px; background: var(--sage); color: var(--paper); font-weight: 700; font-size: 15px; line-height: 26px; text-align: center; }

  .back .brand-circle { left: 148px; top: 20px; width: 124px; height: 124px; border: 1.5px solid var(--gold); }
  .back .brand-name { font-size: 11px; width: 96px; }
  .owner-name { position: absolute; top: 155px; left: 0; width: 420px; text-align: center; font-size: 31px; font-weight: 500; letter-spacing: .01em; }
  .owner-name .first { color: var(--rose-text); font-weight: 700; }
  .owner-role { position: absolute; top: 191px; left: 0; width: 420px; text-align: center; font-size: 17px; letter-spacing: .38em; }
  .contact-icon { position: absolute; left: 192px; width: 36px; height: 36px; border-radius: 50%; background: var(--sage); display: flex; align-items: center; justify-content: center; }
  .contact-text { position: absolute; left: 0; width: 420px; text-align: center; font-size: 15px; }
  .contact-text.phone { font-weight: 700; font-size: 16px; }
  .contact-text b { font-weight: 700; }
  .fb-line { position: absolute; top: 680px; left: 0; width: 420px; text-align: center; font-size: 14px; }
  .fb-line .handle { color: var(--rose-text); font-weight: 600; font-size: 15px; margin-left: 4px; }
</style>
</head>
<body>

<div class="stage"></div>

<!-- Front face template repeated: small preview, then full size -->
<div class="card card--mini front" style="left:247px; top:195px;">
  <svg class="shape" width="420" height="735" viewBox="0 0 420 735">
    <rect width="420" height="735" fill="var(--blush)"/>
    <path d="M0,395 Q210,190 420,395 Q210,255 0,395Z" fill="var(--rose)"/>
    <path d="M0,395 Q210,255 420,395 V735 H0Z" fill="var(--paper)"/>
    <path d="M0,395 Q210,255 420,395" fill="none" stroke="var(--gold)" stroke-width="2"/>
  </svg>
  <div class="brand-circle"><span class="brand-name">MAPLE HOLLOW BLOOM PANELS</span></div>
  <div class="tagline tagline--main">Let us be your</div>
  <div class="tagline tagline--sub"><span class="dot"></span>something extra<span class="dot"></span></div>
  <div class="web-pill">www.maplehollowbloompanels.net</div>
</div>

<div class="card card--mini back" style="left:643px; top:165px;">
  <svg class="shape" width="420" height="735" viewBox="0 0 420 735">
    <rect width="420" height="735" fill="var(--blush)"/>
    <path d="M0,147 Q210,347 420,147Z" fill="var(--rose)"/>
    <path d="M0,147 Q210,347 420,147" fill="none" stroke="var(--gold)" stroke-width="2"/>
    <path d="M0,0 H420 V147 Q210,247 0,147Z" fill="var(--paper)"/>
    <path d="M0,560 Q210,700 420,560 V600 Q210,690 0,600Z" fill="var(--rose)"/>
    <path d="M0,575 Q210,700 420,575" fill="none" stroke="var(--gold)" stroke-width="2"/>
    <path d="M0,580 Q210,690 420,580 V735 H0Z" fill="var(--paper)"/>
  </svg>
  <div class="brand-circle"><span class="brand-name">MAPLE HOLLOW BLOOM PANELS</span></div>
  <div class="owner-name"><span class="first">LENA</span> WHITCOMBE</div>
  <div class="owner-role">OWNER</div>
  <div class="contact-icon" style="top:340px;"><svg width="18" height="18" viewBox="0 0 24 24"><path d="M6.6 10.8a15 15 0 0 0 6.6 6.6l2.2-2.2a1 1 0 0 1 1-.25 11.4 11.4 0 0 0 3.6.57 1 1 0 0 1 1 1V20a1 1 0 0 1-1 1A17 17 0 0 1 3 4a1 1 0 0 1 1-1h3.5a1 1 0 0 1 1 1c0 1.25.2 2.45.57 3.57a1 1 0 0 1-.25 1z" fill="#fff"/></svg></div>
  <div class="contact-text phone" style="top:382px;">401-726-3148</div>
  <div class="contact-icon" style="top:422px;"><svg width="18" height="18" viewBox="0 0 24 24"><rect x="3" y="5" width="18" height="14" rx="2" fill="#fff"/><path d="M3.5 6l8.5 7 8.5-7" fill="none" stroke="var(--sage)" stroke-width="1.6"/></svg></div>
  <div class="contact-text" style="top:465px;">maplehollowbloompanels@mailvane.net</div>
  <div class="contact-icon" style="top:510px;"><svg width="18" height="18" viewBox="0 0 24 24" fill="none" stroke="#fff" stroke-width="1.8"><circle cx="12" cy="12" r="9"/><ellipse cx="12" cy="12" rx="4" ry="9"/><path d="M3 12h18"/></svg></div>
  <div class="contact-text" style="top:552px;">www.<b>maplehollowbloompanels</b>.net</div>
  <div class="fb-line">FB handle<span class="handle">maplehollowbloompanels</span></div>
</div>

<div class="card front" style="left:390px; top:1005px;">
  <svg class="shape" width="420" height="735" viewBox="0 0 420 735">
    <rect width="420" height="735" fill="var(--blush)"/>
    <path d="M0,395 Q210,190 420,395 Q210,255 0,395Z" fill="var(--rose)"/>
    <path d="M0,395 Q210,255 420,395 V735 H0Z" fill="var(--paper)"/>
    <path d="M0,395 Q210,255 420,395" fill="none" stroke="var(--gold)" stroke-width="2"/>
  </svg>
  <div class="brand-circle"><span class="brand-name">MAPLE HOLLOW BLOOM PANELS</span></div>
  <div class="tagline tagline--main">Let us be your</div>
  <div class="tagline tagline--sub"><span class="dot"></span>something extra<span class="dot"></span></div>
  <div class="web-pill">www.maplehollowbloompanels.net</div>
</div>

<div class="card back" style="left:390px; top:1818px;">
  <svg class="shape" width="420" height="735" viewBox="0 0 420 735">
    <rect width="420" height="735" fill="var(--blush)"/>
    <path d="M0,147 Q210,347 420,147Z" fill="var(--rose)"/>
    <path d="M0,147 Q210,347 420,147" fill="none" stroke="var(--gold)" stroke-width="2"/>
    <path d="M0,0 H420 V147 Q210,247 0,147Z" fill="var(--paper)"/>
    <path d="M0,560 Q210,700 420,560 V600 Q210,690 0,600Z" fill="var(--rose)"/>
    <path d="M0,575 Q210,700 420,575" fill="none" stroke="var(--gold)" stroke-width="2"/>
    <path d="M0,580 Q210,690 420,580 V735 H0Z" fill="var(--paper)"/>
  </svg>
  <div class="brand-circle"><span class="brand-name">MAPLE HOLLOW BLOOM PANELS</span></div>
  <div class="owner-name"><span class="first">LENA</span> WHITCOMBE</div>
  <div class="owner-role">OWNER</div>
  <div class="contact-icon" style="top:340px;"><svg width="18" height="18" viewBox="0 0 24 24"><path d="M6.6 10.8a15 15 0 0 0 6.6 6.6l2.2-2.2a1 1 0 0 1 1-.25 11.4 11.4 0 0 0 3.6.57 1 1 0 0 1 1 1V20a1 1 0 0 1-1 1A17 17 0 0 1 3 4a1 1 0 0 1 1-1h3.5a1 1 0 0 1 1 1c0 1.25.2 2.45.57 3.57a1 1 0 0 1-.25 1z" fill="#fff"/></svg></div>
  <div class="contact-text phone" style="top:382px;">401-726-3148</div>
  <div class="contact-icon" style="top:422px;"><svg width="18" height="18" viewBox="0 0 24 24"><rect x="3" y="5" width="18" height="14" rx="2" fill="#fff"/><path d="M3.5 6l8.5 7 8.5-7" fill="none" stroke="var(--sage)" stroke-width="1.6"/></svg></div>
  <div class="contact-text" style="top:465px;">maplehollowbloompanels@mailvane.net</div>
  <div class="contact-icon" style="top:510px;"><svg width="18" height="18" viewBox="0 0 24 24" fill="none" stroke="#fff" stroke-width="1.8"><circle cx="12" cy="12" r="9"/><ellipse cx="12" cy="12" rx="4" ry="9"/><path d="M3 12h18"/></svg></div>
  <div class="contact-text" style="top:552px;">www.<b>maplehollowbloompanels</b>.net</div>
  <div class="fb-line">FB handle<span class="handle">maplehollowbloompanels</span></div>
</div>

</body>
</html>
```